Yacht, Boats, Watersports company needs a redesign of business card

Hello Designers!
We are a Boat dealership company that sells fun in the water, we sell boats, Yachts, Kayaks and also yacht WaterSport toys. We are looking to redesign our business cards in to something a little bit more sophisticated. in a way that we can make better use of our company colors. I'm attaching a zipped file containing the company 3 sets of company logo which one is an horizontal another one is a vertical and also a chromed 3d logo. Also is included two set of business cards that we use and also some designs that i think it's interesting. We use PMS 2026c Orange and PMS 7687C Blue. I would like to see at least two different options with the orange as accent and also using blue as an accent color. It's really important for the business cards to have a font option and size that is legible to most people. Our current website is wwww.corvellamarine.com. Please visit if you want to have a better feeling of the Boat dealership
You can send Single sided or double side options. We are now using single sided but we may be open for a double side option if we really like the design.
Target Market(s)
Marine, boat sales, yacht sales, water toys sales/
Contact Information for Business Card
Name: Dale Pritchett
Address: 718 West Halden Lane,
Dania Beach, FL 33019
Phone: 954-382-7146
Fax: 954:382-7139
Cell: 954-451-8320
Email: 212@corvellamarine.com
Website: corvellamarine.com
Requirements
Must have
- the current information of the business card provided.
logo
use the PMS Colors
Nice to have
- a touch of elegance and sophistication but simple
Should not have
- should not have any typography that is hard to read, the card should be simple but yet sophisticated.

```html
<!DOCTYPE html>
<html lang="en">
<head>
<meta charset="utf-8">
<title>Corvella Marine – Business Card</title>
<link href="https://fonts.googleapis.com/css2?family=Roboto:wght@400;500&family=Roboto+Condensed:wght@700&display=swap" rel="stylesheet">
<style>
  :root {
    --brand-blue: #0f4577;
    --brand-orange: #e85d2f;
    --card-light: #f4f4f4;
    --backdrop: #e2e2e2;
    --white: #ffffff;
  }
  * { margin: 0; padding: 0; box-sizing: border-box; }
  html, body { width: 1200px; height: 960px; overflow: hidden; }
  body {
    position: relative;
    background: var(--backdrop);
    font-family: "Roboto", Arial, sans-serif;
  }
  .card {
    position: absolute;
    left: 307px;
    width: 590px;
    height: 335px;
    overflow: hidden;
  }
  .card--front { top: 118px; background: var(--brand-blue); }
  .card--back { top: 505px; background: var(--card-light); }

  .edge-arrow { position: absolute; }
  .card--front .edge-arrow { left: 0; top: 140px; }
  .card--back .edge-arrow { right: 0; top: 92px; }

  .brand-dot {
    position: absolute;
    left: 75px; top: 126px;
    width: 84px; height: 84px;
    border-radius: 50%;
    border: 6px solid var(--white);
  }
  .brand-name {
    position: absolute;
    left: 181px; top: 145px;
    color: var(--white);
    font-size: 22px;
    font-weight: 500;
    letter-spacing: 2px;
    text-transform: uppercase;
    white-space: nowrap;
  }

  .side-band {
    position: absolute;
    left: 0; top: 0;
    width: 127px; height: 100%;
    background: var(--brand-blue);
  }
  .side-stripe {
    position: absolute;
    left: 127px; top: 0;
    width: 9px; height: 100%;
    background: var(--brand-orange);
  }
  .brand-seal {
    position: absolute;
    left: 45px; top: 82px;
    width: 164px; height: 164px;
    border-radius: 50%;
    background: var(--white);
    display: flex;
    align-items: center;
    justify-content: center;
    text-align: center;
    color: var(--brand-blue);
    font-size: 15px;
    font-weight: 500;
    letter-spacing: 1.5px;
    line-height: 1.3;
    text-transform: uppercase;
  }

  .holder-name {
    position: absolute;
    left: 318px; top: 68px;
    font-family: "Roboto Condensed", "Arial Narrow", sans-serif;
    font-weight: 700;
    font-size: 28px;
    color: var(--brand-blue);
    white-space: nowrap;
  }
  .holder-name .surname { color: var(--brand-orange); }
  .divider {
    position: absolute;
    left: 318px; top: 117px;
    width: 240px; height: 2px;
    background: var(--brand-orange);
  }
  .address {
    position: absolute;
    left: 318px; top: 135px;
    font-size: 16px;
    line-height: 20px;
    color: var(--brand-blue);
    font-style: normal;
  }
  .contact-list {
    position: absolute;
    left: 318px; top: 184px;
    list-style: none;
    font-size: 16px;
    line-height: 19.8px;
    color: var(--brand-blue);
  }
  .contact-list li { display: flex; align-items: center; gap: 5px; white-space: nowrap; }
  .contact-list svg { width: 13px; height: 13px; flex: none; }
</style>
</head>
<body>

<section class="card card--front" aria-label="Card front">
  <svg class="edge-arrow" width="38" height="55" viewBox="0 0 38 55"><polygon points="0,0 38,27.5 0,55" fill="var(--brand-orange)"/></svg>
  <div class="brand-dot"></div>
  <div class="brand-name">Corvella Marine</div>
</section>

<section class="card card--back" aria-label="Card back">
  <div class="side-band"></div>
  <div class="side-stripe"></div>
  <div class="brand-seal">Corvella<br>Marine</div>

  <h1 class="holder-name">Dale <span class="surname">Pritchett</span></h1>
  <div class="divider"></div>
  <svg class="edge-arrow" width="37" height="54" viewBox="0 0 37 54"><polygon points="37,0 0,26 37,54" fill="var(--brand-orange)"/></svg>

  <address class="address">718 West Halden Lane,<br>Dania Beach, FL 33019</address>

  <ul class="contact-list">
    <li><svg viewBox="0 0 16 16"><path d="M3 1l3 3-1.5 2c1 2 3 4 5 5l2-1.5 3 3-2 2C7 14 2 9 1 3z" fill="var(--brand-orange)"/></svg>954-382-7146</li>
    <li><svg viewBox="0 0 16 16"><rect x="4" y="1" width="8" height="4" fill="var(--brand-orange)"/><rect x="1" y="6" width="14" height="6" rx="1" fill="var(--brand-orange)"/><rect x="4" y="10" width="8" height="5" fill="var(--brand-orange)"/></svg>954:382-7139</li>
    <li><svg viewBox="0 0 16 16"><rect x="4" y="1" width="8" height="14" rx="1.5" fill="none" stroke="var(--brand-orange)" stroke-width="1.5"/><circle cx="8" cy="12.5" r="0.9" fill="var(--brand-orange)"/></svg>954-451-8320</li>
    <li><svg viewBox="0 0 16 16"><rect x="1" y="3" width="14" height="10" fill="none" stroke="var(--brand-orange)" stroke-width="1.5"/><path d="M1 3l7 6 7-6M1 13l5-5M15 13l-5-5" fill="none" stroke="var(--brand-orange)" stroke-width="1.3"/></svg>212@corvellamarine.com</li>
    <li><svg viewBox="0 0 16 16"><g fill="none" stroke="var(--brand-orange)" stroke-width="1.2"><circle cx="8" cy="8" r="6.5"/><ellipse cx="8" cy="8" rx="3" ry="6.5"/><path d="M1.5 8h13M3 4.5h10M3 11.5h10"/></g></svg>corvellamarine.com</li>
  </ul>
</section>

</body>
</html>
```